Quorlan Visit cards serious but not sad

Hello, I'd like to design my visit cards with the logo Quorlan (attached) the following information: Name: Mathis Deloraux Title: Mobile Director: 33 (0) 6 28 40 13 85 Phone: 33 (0) 4 71 86 52 09 e-mail: mathis.deloraux@quorlan-advisory.example address: 17 Rue Anatole Berrin 92400 Courbevoie This visit will be used on the banking institutions and Quorlan is a consulting firm. I do not want to have dark background.

Target Market(s)

banks

Contact Information for Business Card

Name : Mathis Deloraux
Title : Director
mobile : +33(0)6 28 40 13 85
Phone : +33(0)4 71 86 52 09
e-mail: mathis.deloraux@quorlan-advisory.example
adresse : 17 Rue anatole Berrin 92400 Courbevoie

Requirements
Nice to have
• serious but not sad

```html
<!DOCTYPE html>
<html lang="en">
<head>
<meta charset="utf-8">
<title>Quorlan business card</title>
<link rel="stylesheet" href="https://fonts.googleapis.com/css2?family=Exo+2:wght@500&family=Roboto:wght@400&display=swap">
<style>
  :root {
    --brand-blue: #275a98;
    --card-white: #f4f4f4;
    --backdrop: #b8b8b8;
    --ink: #333333;
    --on-blue: #f2f4f8;
  }
  * { box-sizing: border-box; margin: 0; padding: 0; }
  html, body { width: 1200px; height: 576px; overflow: hidden; }
  body {
    background: var(--backdrop);
    position: relative;
    font-family: "Roboto", Arial, sans-serif;
    color: var(--ink);
  }
  .card {
    position: absolute;
    top: 138px;
    border-radius: 14px;
  }
  .card-front {
    left: 82px; width: 484px; height: 294px;
    background: var(--brand-blue);
  }
  .card-back {
    left: 602px; width: 481px; height: 292px;
    background: var(--card-white);
  }
  .brand {
    position: absolute;
    display: flex;
    align-items: center;
    font-family: "Exo 2", Arial, sans-serif;
    font-weight: 500;
    line-height: 1;
  }
  .brand-dot { border-radius: 50%; flex: none; }
  .card-front .brand { left: 96px; top: 100px; gap: 14px; color: var(--on-blue); font-size: 52px; }
  .card-front .brand-dot { width: 76px; height: 76px; background: var(--on-blue); }
  .card-back .brand { right: 23px; top: 31px; gap: 12px; color: var(--brand-blue); font-size: 42px; }
  .card-back .brand-dot { width: 76px; height: 76px; background: var(--brand-blue); }

  .website {
    position: absolute; left: 0; right: 0; top: 266px;
    display: flex; justify-content: center; align-items: center; gap: 12px;
    color: var(--on-blue); font-size: 12.5px;
  }
  .website .rule { width: 60px; height: 2px; background: var(--on-blue); opacity: .85; border-radius: 1px; }

  .holder-name {
    position: absolute; left: 22px; top: 154px;
    font-family: "Exo 2", Arial, sans-serif; font-weight: 500;
    font-size: 21px; color: var(--brand-blue); letter-spacing: .2px;
  }
  .holder-title {
    position: absolute; left: 22px; top: 182px; right: 23px;
    display: flex; align-items: flex-end; gap: 5px;
    font-size: 10.5px; color: var(--ink);
  }
  .holder-title .rule { flex: 1; height: 1px; background: var(--brand-blue); margin-bottom: 3px; }

  .contact-list {
    position: absolute; left: 24px; top: 219px;
    list-style: none; font-size: 12.5px; line-height: 16px;
  }
  .contact-list li { display: flex; align-items: center; gap: 7px; }
  .contact-list svg { width: 11px; height: 11px; fill: var(--brand-blue); flex: none; }

  .address {
    position: absolute; right: 23px; top: 235px;
    text-align: right; font-style: normal; font-size: 12.5px; line-height: 16px;
  }
</style>
</head>
<body>
  <section class="card card-front">
    <div class="brand"><span class="brand-dot"></span><span class="brand-name">Quorlan</span></div>
    <p class="website"><span class="rule"></span>www.quorlan-advisory.example<span class="rule"></span></p>
  </section>

  <section class="card card-back">
    <div class="brand"><span class="brand-dot"></span><span class="brand-name">Quorlan</span></div>
    <h1 class="holder-name">Mathis Deloraux</h1>
    <p class="holder-title"><span>Director</span><span class="rule"></span></p>
    <ul class="contact-list">
      <li><svg viewBox="0 0 12 12" aria-hidden="true"><path d="M3 0h6a1 1 0 0 1 1 1v10a1 1 0 0 1-1 1H3a1 1 0 0 1-1-1V1a1 1 0 0 1 1-1zm0.8 1.5v7.5h4.4V1.5zM6 9.8a.7.7 0 1 0 0 1.4.7.7 0 0 0 0-1.4z"/></svg>+33(0)6 28 40 13 85</li>
      <li><svg viewBox="0 0 12 12" aria-hidden="true"><path d="M0 4c0-1.5 2.5-3 6-3s6 1.5 6 3v1H9V4c-.8-.4-1.8-.6-3-.6S3.8 3.6 3 4v1H0zM2.5 6h7l1.5 5H1z"/></svg>+33(0)4 71 86 52 09</li>
      <li><svg viewBox="0 0 12 12" aria-hidden="true"><path d="M0 2h12v1L6 7 0 3zM0 4.2l6 4 6-4V10H0z"/></svg>mathis.deloraux@quorlan-advisory.example</li>
    </ul>
    <address class="address">17 Rue anatole Berrin<br>92150 Lorvenne</address>
  </section>
</body>
</html>
```